Antiseptic products for Veloran East Africa

I need several antiseptic product designs for topical solutions such as surgical spirit, methylated spirit, hand sanitizer, calamine lotion, povidone solution, glycerine, povidone mouthwash, chlorhexidine solution, and sodium hypochlorite solution.

KINDLY START WITH THE HAND SANITIZER DESIGN, URGENT.

Target Market(s)

International market

Industry/Entity Type

Pharmaceutical

Font styles to use
Serif
Script

Colors
33a6d7
3277b5
0758a5
7651a1
886aae
e34197
e667a6
f78f20

Requirements
Must have
• Elegant designs, writtings to appear as they are. safety symbols to appear such as flammable or corrosive.
Nice to have
• Attractive colours but keep it simple and classy.

```html
<!DOCTYPE html>
<html lang="en">
<head>
<meta charset="UTF-8">
<title>Veloran East Africa – Hand Sanitizer Label</title>
<link rel="stylesheet" href="https://fonts.googleapis.com/css2?family=Cormorant+Garamond:wght@500;600&family=Great+Vibes&display=swap">
<style>
  :root {
    --page-bg: #ececec;
    --label-top: #d6f0fa;
    --label-mid: #8ccfea;
    --label-bottom: #33a6d7;
    --ink: #0758a5;
    --ink-soft: #3277b5;
    --accent-violet: #7651a1;
    --accent-pink: #e34197;
    --hazard-orange: #f78f20;
    --hazard-red: #e34197;
    --hazard-fill: #ffffff;
    --aloe-light: #d9ecd2;
    --aloe-dark: #5f9e3e;
    --glow: rgba(255, 255, 255, 0.6);
  }
  * { margin: 0; padding: 0; box-sizing: border-box; }
  html, body {
    width: 1200px;
    height: 800px;
    overflow: hidden;
    background: var(--page-bg);
    font-family: "Cormorant Garamond", serif;
    color: var(--ink);
  }
  .canvas {
    position: relative;
    width: 1200px;
    height: 800px;
  }
  .label {
    position: absolute;
    left: 380px;
    top: 40px;
    width: 440px;
    height: 720px;
    border-radius: 10px;
    overflow: hidden;
    background:
      radial-gradient(circle at 50% 14%, var(--glow) 0, rgba(255,255,255,0) 45%),
      linear-gradient(180deg, var(--label-top) 0%, var(--label-mid) 50%, var(--label-bottom) 100%);
  }
  .brand {
    position: absolute;
    top: 112px;
    left: 0;
    width: 100%;
    display: flex;
    justify-content: center;
    align-items: center;
    gap: 10px;
  }
  .brand-dot {
    width: 16px;
    height: 16px;
    border-radius: 50%;
    background: var(--accent-violet);
  }
  .brand-name {
    font-size: 38px;
    font-weight: 600;
    line-height: 1;
    color: var(--ink);
  }
  .region {
    position: absolute;
    top: 178px;
    width: 100%;
    text-align: center;
    font-family: "Great Vibes", cursive;
    font-size: 50px;
    line-height: 1.1;
    color: var(--ink-soft);
  }
  .product-name {
    position: absolute;
    top: 290px;
    width: 100%;
    text-align: center;
    font-size: 50px;
    font-weight: 600;
    line-height: 1.1;
    color: var(--ink);
  }
  .product-benefits {
    position: absolute;
    top: 376px;
    width: 100%;
    text-align: center;
    font-size: 26px;
    line-height: 1.2;
    font-weight: 500;
    color: var(--ink);
  }
  .aloe-artwork {
    position: absolute;
    left: 0;
    bottom: 0;
    width: 300px;
    height: 230px;
    border-top-right-radius: 140px 120px;
    background: linear-gradient(160deg, var(--aloe-dark) 0%, var(--aloe-light) 100%);
  }
  .hazard-flammable {
    position: absolute;
    right: 28px;
    bottom: 92px;
    width: 78px;
    height: 78px;
  }
  .volume {
    position: absolute;
    right: 24px;
    bottom: 26px;
    font-size: 36px;
    font-weight: 600;
    line-height: 1;
    color: var(--ink);
  }
</style>
</head>
<body>
  <main class="canvas">
    <section class="label">
      <div class="brand">
        <span class="brand-dot"></span>
        <span class="brand-name">Veloran</span>
      </div>
      <p class="region">East Africa</p>
      <h1 class="product-name">Hand Sanitizer</h1>
      <p class="product-benefits">With vitamin E<br>&amp; Aloevera</p>
      <div class="aloe-artwork" role="img" aria-label="Illustration of aloe vera leaves and sliced aloe pieces"></div>
      <svg class="hazard-flammable" viewBox="0 0 100 100" role="img" aria-label="Flammable hazard symbol">
        <polygon points="50,4 96,50 50,96 4,50" fill="var(--hazard-fill)" stroke="var(--hazard-red)" stroke-width="7" stroke-linejoin="round"/>
        <path d="M50 24 C58 36 66 42 64 56 C63 66 57 72 50 72 C42 72 36 66 36 57 C36 49 41 45 44 40 C45 46 47 49 50 50 C52 42 52 33 50 24 Z" fill="#1a1a1a"/>
        <rect x="34" y="74" width="32" height="5" rx="1" fill="#1a1a1a"/>
      </svg>
      <p class="volume">15 ml</p>
    </section>
  </main>
</body>
</html>
```